Executive Performance Review mapped on J-curve

I need to turn an executive company performance review into a visual infographic. The list of accomplishments is grouped into four calendar quarters. Each quarter needs a subtle representation of the season. The four quarters and associated list of accomplishments need to be mapped to a J-curve. - Spreadsheet with accomplishments attached (Throughput)- Sample image of a J-curve. You can google J-curve to see more images.- The title should be "Danela Morsky Year in Review"

Target Market(s)

Board of Directors

Requirements
Nice to have
• This will be presented to a company founder that is an artist and customer experience expert. He is very visual so a nice visual representation of the data will be impactful. He also uses the phrase that you have to live with or work with someone for four seasons before you really know them. This is why I have the seasons mapped to the quarters. The Fall season motif should be gloomy and stormy.

```html
<!DOCTYPE html>
<html lang="en">
<head>
<meta charset="utf-8">
<title>Danela Morsky Year in Review</title>
<link href="https://fonts.googleapis.com/css2?family=Archivo:wght@800&family=Source+Sans+3:wght@300;400;700&display=swap" rel="stylesheet">
<style>
  :root{
    --ink:#3a3a3a;
    --text:#222;
    --summer-bg:#fdf4c9;
    --fall-bg:#d1d4d7;
    --winter-bg:#eefafc;
    --spring-bg:#f3f8e3;
    --summer:#fcd20a;
    --fall:#535d66;
    --winter:#d5f0f9;
    --spring:#c4de55;
    --white:#fff;
  }
  *{margin:0;padding:0;box-sizing:border-box}
  html,body{width:1200px;height:700px;overflow:hidden;background:var(--white)}
  body{position:relative;font-family:"Source Sans 3",Arial,sans-serif;color:var(--text)}
  .masthead{position:absolute;top:14px;left:0;width:1234px;text-align:center;color:var(--ink)}
  .masthead h1{font-family:"Archivo",Arial,sans-serif;font-weight:800;font-size:31px;letter-spacing:.2px;line-height:36px}
  .masthead .subtitle{font-weight:300;font-size:28px;line-height:30px}
  .masthead .company{font-weight:300;font-size:20px;line-height:24px}
  .stage{position:absolute;left:0;top:0}
  .quarter{position:absolute;top:124px;padding:9px 7px;font-size:10px;line-height:14.6px}
  .quarter h2{font-size:10px;font-weight:700;line-height:14.6px;text-transform:uppercase}
  .quarter ul{list-style:none;margin-bottom:10px}
  .quarter li::before{content:"• "}
  .quarter p{margin-bottom:0}
  .quarter .block{margin-bottom:10px}
  .q-summer{left:27px;width:230px}
  .q-fall{left:257px;width:229px}
  .q-winter{left:486px;width:229px}
  .q-spring{left:715px;width:250px}
  .q-future{left:961px;width:210px}
  .season-label{position:absolute;top:653px;font-size:10px;font-weight:700;text-align:center;text-transform:uppercase;line-height:14px}
  .season-label.on-dark{color:var(--white)}
</style>
</head>
<body>
  <svg class="stage" width="1200" height="700" viewBox="0 0 1200 700" aria-hidden="false">
    <defs>
      <linearGradient id="ground" x1="27" y1="0" x2="1175" y2="0" gradientUnits="userSpaceOnUse">
        <stop offset="0" stop-color="#fcd20a"/>
        <stop offset="0.19" stop-color="#f7c800"/>
        <stop offset="0.21" stop-color="#58626b"/>
        <stop offset="0.38" stop-color="#4d5760"/>
        <stop offset="0.42" stop-color="#d5f0f9"/>
        <stop offset="0.56" stop-color="#c6e9f4"/>
        <stop offset="0.64" stop-color="#d9eec6"/>
        <stop offset="0.8" stop-color="#c9e27a"/>
        <stop offset="1" stop-color="#c1dc4e"/>
      </linearGradient>
      <linearGradient id="rise" x1="0" y1="124" x2="0" y2="520" gradientUnits="userSpaceOnUse">
        <stop offset="0" stop-color="#c6df5e"/>
        <stop offset="1" stop-color="#d8ea9a"/>
      </linearGradient>
    </defs>
    <rect class="panel-summer" x="27" y="124" width="230" height="543" fill="var(--summer-bg)"/>
    <rect class="panel-fall" x="257" y="124" width="229" height="543" fill="var(--fall-bg)"/>
    <rect class="panel-winter" x="486" y="124" width="229" height="543" fill="var(--winter-bg)"/>
    <rect class="panel-spring" x="715" y="124" width="460" height="543" fill="var(--spring-bg)"/>
    <path class="j-curve-ground" role="img" aria-label="Seasonal scenery along the J-curve: sunny beach with palms, stormy rain clouds and falling leaves, snowy landscape with snowman, and a spring meadow with flowers, butterflies and a bird"
      d="M27,516 C120,540 200,600 300,590 C600,560 950,380 1175,124 L1175,667 L27,667 Z" fill="url(#ground)"/>
    <path class="j-curve-line" d="M27,516 C120,540 200,600 300,590 C600,560 950,380 1175,124" fill="none" stroke="#ffffff" stroke-opacity=".5" stroke-width="1.5"/>
  </svg>

  <header class="masthead">
    <h1>DANELA MORSKY - YEAR ONE IN</h1>
    <div class="subtitle">JULY 1, 2019 REVIEW</div>
    <div class="company">VANTOR LABS, INC.</div>
  </header>

  <section class="quarter q-summer">
    <h2>Transitions</h2>
    <ul>
      <li>RO Transition from Rowan &amp; Lena</li>
      <li>Start DM Office Initiative</li>
      <li>Tactical Ops transition from Rowan</li>
      <li>Formalize Exec Team</li>
    </ul>
    <h2>Biz Architecture</h2>
    <ul>
      <li>Independent Financial Audit</li>
      <li>Organizational Audit - Structure</li>
      <li>Organizational Audit - People</li>
      <li>XF Framework - ESU</li>
      <li>Defined Utilization, Realization, Availability</li>
    </ul>
    <h2>Strategy</h2>
    <ul>
      <li>Effective Strategy Meeting</li>
      <li>Strategic Themes 2018 - 2020: Stablize, Accel-erate, Surge</li>
      <li>Business Drivers: Drive Revenue, Improve Vantorite Experience, Increase Brand Awareness</li>
    </ul>
    <h2>Sales</h2>
    <ul>
      <li>Halbridge Account Transition</li>
      <li>ERV Account Transition</li>
      <li>2 year Managed Services Engagement Model</li>
    </ul>
    <h2>Revenue / EBITA</h2>
    <ul><li>TBD</li></ul>
  </section>

  <section class="quarter q-fall">
    <h2>Biz Architecture</h2>
    <ul>
      <li>XF Framework - Functional Meetings &amp;</li>
      <li>Scrum of Scrums</li>
      <li>Structured Reorg</li>
      <li>Implemented Reorg</li>
      <li>Quarterly Org Iteration cadence</li>
      <li>Defined Key Hire Plan</li>
      <li>DM Office Operational</li>
      <li>Time Accountability</li>
      <li>Tools ReConfig</li>
      <li>Org Structure v1</li>
    </ul>
    <h2>Strategy</h2>
    <ul><li>Internal QBR Accountability</li></ul>
    <h2>Sales</h2>
    <ul>
      <li>Kestrel QBR</li>
      <li>Halbridge QBR</li>
    </ul>
    <h2>Revenue / EBITA</h2>
    <ul><li>TBD</li></ul>
  </section>

  <section class="quarter q-winter">
    <h2>Biz Architecture</h2>
    <ul>
      <li>XF Framework - Progress Demos</li>
      <li>Org Structure - COE's</li>
      <li>Stablize Accounting &amp; Finance</li>
      <li>Exec Hiring Process</li>
    </ul>
    <h2>Key Hires</h2>
    <ul>
      <li>Controller</li>
      <li>Director CX</li>
    </ul>
    <h2>Strategy</h2>
    <ul>
      <li>Founders removed from front line activity</li>
      <li>Vantor QBR - Goal Setting &amp; Tracking</li>
    </ul>
    <h2>Sales</h2>
    <div class="block"><p>ERV QBR</p><p>Halbridge QBR</p></div>
    <h2>Revenue / EBITA</h2>
    <div class="block"><p>TBD</p></div>
  </section>

  <section class="quarter q-spring">
    <h2>Biz Architecture</h2>
    <ul>
      <li>Tiered Pricing Pre-Paid Engagement Model</li>
      <li>XF Framework - Ideation Board</li>
      <li>Consulting Levels &amp; Salary Bands</li>
      <li>Roles &amp; Responsibilities</li>
    </ul>
    <h2>Key Hires</h2>
    <ul>
      <li>Interim HR</li>
      <li>Provisional Client Partner</li>
      <li>Acting Director 1</li>
      <li>Acting Director 2</li>
      <li>Client Partner 1</li>
      <li>Sales Exec 1</li>
    </ul>
    <h2>Sales</h2>
    <ul>
      <li>Opened BrightFrame Door</li>
      <li>Flipped focus from operationaly<br>run company to sales/marketing<br>driven org</li>
      <li>NPA Direct</li>
    </ul>
    <h2>Revenue / EBITA</h2>
    <ul><li>TBD</li></ul>
  </section>

  <section class="quarter q-future">
    <h2>• Greenfield</h2>
  </section>

  <div class="season-label" style="left:27px;width:230px">Summer: Q3 2018 - Assessment</div>
  <div class="season-label on-dark" style="left:257px;width:229px">Fall: Q4 2018 - Stablize</div>
  <div class="season-label" style="left:486px;width:229px">Winter: Q1 2019 - Stratactical</div>
  <div class="season-label" style="left:715px;width:230px">Spring: Q2 2019 - Strategic</div>
  <div class="season-label" style="left:945px;width:230px">2020+: Value Creation</div>
</body>
</html>
```